Business Card for Restaurant Nuvelo

This project consist of creating 2 design for business card of restaurant named Nuvelo.

The attached specs below are 'ONLY SUGGESTION' if you have others ideas. You are welcome to post it.

1) Restaurant Card

Adresse:
2318 Rue des Pruniers
Montréal (Qc) H3K 2T8

Website:
www.nu-velo.ca

Phone:
438-552-0194

2) Employee Card

Name: Greta Lund
Title: Owner

Address:
2318 Rue des Pruniers
Montréal (Qc) H3K 2T8

Email:greta@nu-velo.ca
Phone Number:438-552-0194
Cellphone Number:514-730-4816

 The attached specs are 'ONLY SUGGESTION' if you have others ideas.  You are welcome to post it.

Industry/Entity Type

Restaurant

Requirements
Must have
• UV Card Spot

To print Spot UV business cards you would have to submit 2 files for each side. The first file "base" would be your regular design file as it would have been in any other case. The 2nd file "UV mask" is a black/white file. The BLACK color will indicate the areas that will be covered with the UV high gloss finish. To upload the files, please combine front design and front mask file in one P
Nice to have
• 1) The font of the logo should be ink effect
2) black background with wallpaper effect
3) The specs below are 'ONLY SUGGESTION' if you have others ideas. You are welcome to post it.

```html
<!DOCTYPE html>
<html lang="fr">
<head>
<meta charset="utf-8">
<title>Nuvelo – Cartes d'affaires</title>
<link rel="stylesheet" href="https://fonts.googleapis.com/css2?family=Noto+Sans+JP:wght@400;500&family=Questrial&display=swap">
<style>
  :root {
    --page: #fdeed8;
    --card-white: #ffffff;
    --card-black: #1f1f1f;
    --card-black-edge: #2b2b2b;
    --ink: #1a1a1a;
    --red: #e8382a;
    --white: #ffffff;
    --shadow: rgba(60, 40, 20, 0.45);
    --lantern-light: #9a9a9a;
    --lantern-dark: #2a2a2a;
  }
  * { margin: 0; padding: 0; box-sizing: border-box; }
  html, body { width: 845px; height: 1200px; overflow: hidden; }
  body {
    background: var(--page);
    position: relative;
    font-family: "Questrial", "Century Gothic", sans-serif;
  }
  .card {
    position: absolute;
    left: 182px;
    width: 486px;
    height: 314px;
    box-shadow: 4px 5px 6px var(--shadow);
    overflow: hidden;
  }
  .card--front { top: 167px; background: var(--card-white); }
  .card--back {
    top: 556px;
    background: repeating-linear-gradient(90deg, var(--card-black) 0 3px, var(--card-black-edge) 3px 4px, var(--card-black) 4px 9px);
  }

  .front__kana {
    position: absolute;
    left: 53px;
    top: 22px;
    font-family: "Noto Sans JP", sans-serif;
    font-weight: 500;
    font-size: 33px;
    color: var(--ink);
    letter-spacing: 1px;
  }
  .contact {
    position: absolute;
    right: 159px;
    top: 86px;
    text-align: right;
    color: var(--ink);
    font-size: 16px;
    line-height: 18px;
  }
  .contact__item { margin-bottom: 7px; }
  .contact__label {
    display: block;
    font-size: 8px;
    line-height: 10px;
    margin-bottom: 3px;
    color: var(--ink);
  }
  .contact__label::before,
  .contact__label::after {
    content: "";
    display: inline-block;
    width: 4px; height: 4px;
    border-radius: 50%;
    background: var(--red);
    vertical-align: middle;
    margin: 0 1px;
  }
  .front__lantern {
    position: absolute;
    left: 366px;
    top: 22px;
    width: 66px;
    height: 232px;
  }

  .back__lantern {
    position: absolute;
    left: 0;
    top: 85px;
    width: 200px;
    height: 229px;
  }
  .logo {
    position: absolute;
    left: 192px;
    top: 72px;
    display: flex;
    align-items: center;
    gap: 10px;
  }
  .logo__name {
    font-size: 76px;
    line-height: 1;
    color: var(--white);
    letter-spacing: 1px;
  }
  .logo__dot {
    width: 16px; height: 16px;
    border-radius: 50%;
    background: var(--red);
    align-self: flex-start;
    margin-top: 4px;
  }
  .tagline {
    position: absolute;
    left: 201px;
    top: 183px;
    font-size: 13.5px;
    color: var(--white);
    letter-spacing: 0.3px;
  }
  .tagline__sep { color: var(--red); margin: 0 3px; }
  .back__kana {
    position: absolute;
    left: 412px;
    top: 182px;
    font-family: "Noto Sans JP", sans-serif;
    font-size: 20px;
    line-height: 22px;
    color: var(--red);
    writing-mode: vertical-rl;
  }
</style>
</head>
<body>

  <section class="card card--front" aria-label="Recto de la carte">
    <p class="front__kana">ヌヴェロ</p>

    <div class="contact">
      <div class="contact__item">
        <span class="contact__label">A</span>
        2318 Rue des Pruniers<br>Montréal (Qc) H3K 2T8
      </div>
      <div class="contact__item">
        <span class="contact__label">T</span>
        (514) 438-552-0194
      </div>
      <div class="contact__item">
        <span class="contact__label">W</span>
        www.nu-velo.ca
      </div>
      <div class="contact__item">
        <span class="contact__label">E</span>
        info@nu-velo.ca
      </div>
    </div>

    <svg class="front__lantern" viewBox="0 0 66 232" role="img" aria-label="Illustration d'une lanterne rouge japonaise portant l'inscription izakaya au pinceau">
      <defs>
        <radialGradient id="lanternRed" cx="50%" cy="50%" r="60%">
          <stop offset="0%" stop-color="#f04a35"/>
          <stop offset="100%" stop-color="#e0301f"/>
        </radialGradient>
      </defs>
      <ellipse cx="33" cy="145" rx="29" ry="86" fill="url(#lanternRed)"/>
    </svg>
  </section>

  <section class="card card--back" aria-label="Verso de la carte">
    <svg class="back__lantern" viewBox="0 0 200 229" role="img" aria-label="Illustration d'une lanterne en papier grise en fondu">
      <defs>
        <linearGradient id="lanternGrey" x1="0" x2="1" y1="0" y2="0">
          <stop offset="0%" stop-color="var(--lantern-light)"/>
          <stop offset="60%" stop-color="#6a6a6a"/>
          <stop offset="100%" stop-color="var(--lantern-dark)" stop-opacity="0"/>
        </linearGradient>
      </defs>
      <path d="M0 40 Q120 20 190 120 Q200 180 180 229 L0 229 Z" fill="url(#lanternGrey)"/>
    </svg>

    <div class="logo">
      <span class="logo__name">Nuvelo</span>
      <span class="logo__dot"></span>
    </div>

    <p class="tagline">Resto-Bar Japonais<span class="tagline__sep">·</span>Izakaya<span class="tagline__sep">·</span></p>
    <p class="back__kana">ヌヴェロ</p>
  </section>

</body>
</html>
```